letterhead design for a investing company*

Design an appealing business letterhead to match with our existing logo and attract new customers. Our customers are mainly corporate managers which are detail oriented and judge the company ability to perform a good service based on small details. A professional letterhead will give a good first impression.

Target Market(s)

New customers and business owners

Industry/Entity Type

Marketplace

Font styles to use
Sans Serif
Script

Requirements
Must have
• Must be a professional and elegant design that attracts interest from people who receives it

```html
<!DOCTYPE html>
<html lang="en">
<head>
<meta charset="utf-8">
<title>Corvane Letterhead</title>
<link href="https://fonts.googleapis.com/css2?family=Arimo:wght@400;700&display=swap" rel="stylesheet">
<style>
  :root {
    --navy: #141f40;
    --gold: #ffb800;
    --paper: #ffffff;
    --backdrop: #f0f0f1;
    --edge: #d9d9dc;
    --ink-soft: #3a3f55;
  }
  * { margin: 0; padding: 0; box-sizing: border-box; }
  html, body {
    width: 1200px;
    height: 1000px;
    overflow: hidden;
    background: var(--backdrop);
  }
  .letterhead {
    position: absolute;
    left: 305px;
    top: 79px;
    width: 595px;
    height: 842px;
    background: var(--paper);
    border: 1px solid var(--edge);
    border-right: none;
  }
  .side-band {
    position: absolute;
    top: -1px;
    right: 0;
    width: 16px;
    height: 843px;
  }
  .brand {
    position: absolute;
    left: 36px;
    top: 32px;
    display: flex;
    align-items: center;
    gap: 12px;
  }
  .brand-dot {
    width: 40px;
    height: 40px;
    border-radius: 50%;
    background: var(--gold);
  }
  .brand-name {
    font-family: "Arimo", sans-serif;
    font-weight: 700;
    font-size: 42px;
    letter-spacing: -0.5px;
    color: var(--navy);
    line-height: 1;
  }
  .contact {
    position: absolute;
    right: 41px;
    top: 22px;
    list-style: none;
    text-align: right;
    font-family: "Arimo", sans-serif;
    font-size: 9px;
    color: var(--ink-soft);
  }
  .contact li {
    line-height: 19px;
  }
</style>
</head>
<body>
  <main class="letterhead">
    <header>
      <div class="brand">
        <span class="brand-dot" aria-hidden="true"></span>
        <span class="brand-name">Corvane</span>
      </div>
      <ul class="contact">
        <li>48 Elm Street</li>
        <li>Somewhere 2810</li>
        <li>marcelo@corvane.com</li>
        <li>Tel: +3300 555 0142</li>
      </ul>
    </header>
    <svg class="side-band" viewBox="0 0 16 843" aria-hidden="true">
      <rect x="0" y="0" width="16" height="97" fill="var(--navy)"/>
      <rect x="0" y="97" width="16" height="746" fill="var(--gold)"/>
    </svg>
  </main>
</body>
</html>
```